Email Signatures

I would like to create a new email signature for my team. The design will be the same for everyone, with only individual details such as name and email changing. You can also see our brand style on our website. https://www.tlmbespokehomes.com.au/

Target Market(s)

Clients for new builds or renovations

Industry/Entity Type

Construction

Colors

Designer to choose colors to be used in the design.

```html
<!DOCTYPE html>
<html lang="en">
<head>
<meta charset="utf-8">
<title>TLM Bespoke Homes – Email Signature</title>
<link rel="stylesheet" href="https://fonts.googleapis.com/css2?family=Oswald:wght@300;400;700&display=swap">
<style>
  :root {
    --band: #484848;
    --green: #0a7b3e;
    --white: #ffffff;
    --paper: #ffffff;
  }
  html, body {
    margin: 0;
    padding: 0;
    overflow: hidden;
    background: var(--paper);
  }
  .signature {
    position: relative;
    width: 1200px;
    height: 338px;
    overflow: hidden;
    background: var(--paper);
    font-family: "Oswald", sans-serif;
    color: var(--white);
  }
  .signature__shapes {
    position: absolute;
    inset: 0;
  }
  .brand-name {
    position: absolute;
    left: 60px;
    top: 92px;
    width: 300px;
    font-weight: 700;
    font-size: 112px;
    line-height: 1;
    letter-spacing: 4px;
    margin: 0;
    text-align: center;
  }
  .location-tag {
    position: absolute;
    left: 60px;
    top: 229px;
    width: 271px;
    height: 48px;
    background: var(--green);
    display: flex;
    align-items: center;
    justify-content: center;
    font-weight: 300;
    font-size: 21px;
    letter-spacing: 0.2px;
    transform: scaleX(0.82);
    transform-origin: left center;
    width: 330px;
  }
  .contact-line {
    position: absolute;
    left: 404px;
    top: 124px;
    font-weight: 300;
    font-size: 24px;
    line-height: 1;
    white-space: nowrap;
    transform: scaleX(0.76);
    transform-origin: left top;
  }
  .contact-line a {
    color: inherit;
    text-decoration: none;
  }
  .person-name {
    position: absolute;
    left: 402px;
    top: 148px;
    margin: 0;
    font-weight: 700;
    font-size: 72px;
    line-height: 1;
    letter-spacing: 1px;
    white-space: nowrap;
    transform: scaleX(0.86);
    transform-origin: left top;
  }
  .person-role {
    position: absolute;
    left: 402px;
    top: 208px;
    margin: 0;
    font-weight: 300;
    font-size: 56px;
    line-height: 1;
    white-space: nowrap;
    transform: scaleX(0.78);
    transform-origin: left top;
  }
</style>
</head>
<body>
  <div class="signature">
    <svg class="signature__shapes" width="1200" height="338" viewBox="0 0 1200 338" aria-hidden="true">
      <polygon class="band" points="0,92 1117,92 1086,292 0,292" fill="var(--band)"/>
      <polygon class="accent-bar" points="1130,52 1149,55 1106,332 1087,330" fill="var(--green)"/>
    </svg>

    <p class="brand-name">TLM</p>
    <div class="location-tag">HOBART / TASMANIA / AUSTRALIA</div>

    <div class="contact-line">
      <a href="mailto:info@tlmbespokehomes.com.au">INFO@TLMBESPOKEHOMES.COM.AU</a> / <a href="tel:0400123456">0400-123-456</a>
    </div>
    <h1 class="person-name">LIAM HARTLEY</h1>
    <p class="person-role">GENERAL MANAGER</p>
  </div>
</body>
</html>
```